PDF flyer to go out to Medical Providers: 2 sided A4

We need to design a 2 sided A4 pamphlet which we can email out to prospective clients.

We are a recruitment company and wish to provide staff to healthcare providers

We are a medical recruitment agency. We need to be able to write approximately 600 words, split up into 4 sub headings. Text has been provided on the uploaded word document. THIS TEXT IS DRAFT ONLY AND WILL CHANGE.

We need to look professional & efficient

Target Market(s)

Hospitals, srugeries

Industry/Entity Type

Medical

Requirements
Must have
• Room for 600 words, which will b echanged once the layout is confirmed
Nice to have
• Have it in Word form so we can use it for subsequent mail outs.

```html
<!DOCTYPE html>
<html lang="en">
<head>
<meta charset="utf-8">
<title>Meridian Nursing – Specialist Nursing Recruitment</title>
<link href="https://fonts.googleapis.com/css2?family=Roboto+Condensed:wght@400;700&family=Oswald:wght@500;600&display=swap" rel="stylesheet">
<style>
  :root {
    --sky-light: #e6f6fc;
    --sky-mid: #bfe8f6;
    --sky-deep: #8fd2ec;
    --teal: #0f7c80;
    --teal-dark: #0b5f66;
    --swoosh: #1f8ea3;
    --slate: #4b5968;
    --white: #ffffff;
    --photo-a: #c9d9e6;
    --photo-b: #9fb9cf;
  }
  * { box-sizing: border-box; margin: 0; padding: 0; }
  html, body { width: 848px; height: 1200px; overflow: hidden; }
  body {
    position: relative;
    font-family: "Roboto Condensed", "Arial Narrow", sans-serif;
    background: linear-gradient(160deg, var(--sky-light) 0%, var(--sky-mid) 55%, var(--sky-deep) 100%);
    color: var(--slate);
  }
  .frame-outer, .frame-inner { position: absolute; border: 3px solid var(--white); }
  .frame-outer { left: 20px; top: 20px; right: 20px; bottom: 20px; }
  .frame-inner { left: 30px; top: 30px; right: 30px; bottom: 30px; border-width: 2px; }

  .masthead {
    position: absolute; left: 36px; top: 33px; width: 776px; height: 215px;
    background: linear-gradient(180deg, var(--white) 75%, rgba(255,255,255,0) 100%);
  }
  .photo { position: absolute; }
  .photo-team {
    left: 37px; top: 32px; width: 257px; height: 182px;
    background: linear-gradient(180deg, #dfe8ef 0%, #9ec4dc 100%);
  }
  .brand {
    position: absolute; left: 318px; top: 56px;
    display: flex; align-items: center; gap: 22px;
  }
  .brand-mark { width: 84px; height: 84px; border-radius: 50%; background: var(--teal-dark); flex: none; }
  .brand-name {
    font-family: "Roboto Condensed", sans-serif; font-weight: 700;
    font-size: 44px; line-height: 46px; color: var(--teal-dark);
  }
  .swoosh { position: absolute; left: 36px; top: 205px; width: 776px; height: 85px; }

  .tagline {
    position: absolute; left: 237px; top: 264px;
    font-family: "Oswald", sans-serif; font-weight: 600; font-size: 21px;
    color: var(--teal); letter-spacing: 0.2px; white-space: nowrap;
  }
  .intro {
    position: absolute; left: 64px; top: 310px; width: 622px;
    font-weight: 700; font-size: 17.5px; line-height: 24.5px;
  }
  .intro p + p { margin-top: 24.5px; }

  .section-title {
    font-family: "Oswald", sans-serif; font-weight: 600; font-size: 27px;
    color: var(--teal); text-transform: uppercase; line-height: 1.2;
  }
  .specialisms { position: absolute; left: 75px; top: 566px; width: 440px; }
  .specialisms .lead {
    margin-top: 22px; width: 425px;
    font-weight: 700; font-size: 17.5px; line-height: 25px;
  }
  .specialism-list { list-style: none; margin-top: 14px; }
  .specialism-list li {
    position: relative; padding-left: 26px; margin-bottom: 12px;
    font-weight: 700; font-size: 20px; line-height: 24.5px;
    color: var(--teal); font-variant: small-caps;
  }
  .specialism-list li::before {
    content: ""; position: absolute; left: 4px; top: 9px;
    width: 8px; height: 8px; background: var(--teal); transform: rotate(45deg);
  }

  .photo-framed { border: 4px solid var(--white); }
  .photo-child { left: 542px; top: 599px; width: 187px; height: 232px;
    background: linear-gradient(160deg, #eef2f5 0%, var(--photo-b) 100%); }
  .photo-theatre { left: 383px; top: 789px; width: 234px; height: 155px;
    background: linear-gradient(160deg, #d6e2e8 0%, #8fb8c9 100%); }
  .photo-elderly { left: 615px; top: 803px; width: 175px; height: 240px;
    background: linear-gradient(160deg, var(--photo-a) 0%, #6f87b3 100%); }

  .badge-247 { position: absolute; left: 150px; top: 1046px; width: 139px; height: 77px;
    border-radius: 38px; background: #c7d3e0; }
  .service { position: absolute; left: 318px; top: 1036px; width: 445px; }
  .service .section-title { font-size: 25px; }
  .service p { margin-top: 8px; font-weight: 700; font-size: 17.5px; line-height: 24.5px; }
</style>
</head>
<body>
  <div class="frame-outer"></div>
  <div class="frame-inner"></div>

  <header class="masthead"></header>
  <div class="photo photo-team" role="img" aria-label="Group of smiling nurses and doctors in scrubs"></div>
  <div class="brand">
    <span class="brand-mark"></span>
    <span class="brand-name">Meridian<br>Care Staff</span>
  </div>
  <svg class="swoosh" viewBox="0 0 776 85" preserveAspectRatio="none" aria-hidden="true">
    <path d="M0 70 Q 390 -15 776 62 L776 68 Q 390 5 0 80 Z" fill="#1f8ea3"/>
    <path d="M0 80 Q 390 5 776 68 L776 85 L0 85 Z" fill="rgba(255,255,255,0.3)"/>
  </svg>

  <h1 class="tagline">A SPECIALIST TEAM DEDICATED TO SPECIAL CARE</h1>

  <section class="intro">
    <p>Meridian Nursing was established with a sole focus to provide nationwide recruitment solutions for specialist sector nursing requirements. We have over 30 years industry experience and successfully deliver nursing solutions to client requirements.</p>
    <p>Our philosophy is to be masters in our supply of specialist staff rather than diluting our service by over generalising. This ethos was naturally birthed from supplying to all types of healthcare establishments and identifying a trend whereby agencies could fill easier bookings - still leaving the client with those important and hard to fill requirements and ultimately falling short of providing a full service.</p>
  </section>

  <section class="specialisms">
    <h2 class="section-title">Our Specialisms:</h2>
    <p class="lead">Our consultants provide a professional and effective service in the supply of the following speciality nurses:</p>
    <ul class="specialism-list">
      <li>Theatre (Scrub, Anaesthetics, Recovery)<br>and ODP's</li>
      <li>A&amp;E Nurses</li>
      <li>ITU / HDU / CCU Nurses</li>
      <li>Paediatric Nurses<br>(General Paeds, PICU &amp; NICU)</li>
      <li>RMN &amp; CPN's</li>
      <li>Oncology Nurses</li>
      <li>Community / District Nurses</li>
      <li>Midwives</li>
    </ul>
  </section>

  <div class="photo photo-framed photo-child" role="img" aria-label="Nurse caring for a young child in a hospital bed"></div>
  <div class="photo photo-framed photo-theatre" role="img" aria-label="Theatre staff in scrubs talking together"></div>
  <div class="photo photo-framed photo-elderly" role="img" aria-label="Nurse comforting an elderly patient"></div>

  <div class="badge-247" role="img" aria-label="24/7 clock emblem"></div>
  <section class="service">
    <h2 class="section-title">24 Hour Service:</h2>
    <p>Our consultants are available 24hrs round the clock to manage requests: Last minute adhoc, long/short term bookings, block bookings and pre-approved rotas.</p>
  </section>
</body>
</html>
```